Business Card Design Project

Small privately owned salon.

Industry/Entity Type

Business

Contact Information for Business Card

Hair salon.i would like my logo to be my name , Marisol Denby. Address and phone can go on the front or back. The back will be where I write their appt.
address-362 Thistledown lane York, Pa. 17488
Phone- 717-555-0148

```html
<!DOCTYPE html>
<html lang="en">
<head>
<meta charset="utf-8">
<title>Marisol Denby – Salon Business Card</title>
<link href="https://fonts.googleapis.com/css2?family=Open+Sans:wght@400;600;700&family=Pinyon+Script&display=swap" rel="stylesheet">
<style>
  :root {
    --backdrop: #3b3431;
    --card-black: #0c0c0c;
    --card-edge: #1a1a1a;
    --gold: #f2d21a;
    --gold-deep: #c9a90e;
    --text-light: #f1f1f1;
    --band-white: #ffffff;
    --ink: #111111;
    --dots: #555555;
  }
  * { box-sizing: border-box; margin: 0; padding: 0; }
  html, body {
    width: 1200px; height: 900px; overflow: hidden;
    background: var(--backdrop);
    font-family: "Open Sans", Arial, sans-serif;
  }
  .canvas {
    position: relative; width: 1200px; height: 900px;
    display: flex; align-items: center; justify-content: center; gap: 60px;
  }
  .card {
    position: relative; width: 525px; height: 300px;
    background: var(--card-black);
    border: 1px solid var(--card-edge);
    border-radius: 4px;
    overflow: hidden;
    box-shadow: 0 14px 30px rgba(0,0,0,.45);
  }

  /* Front */
  .card-front .salon-name {
    position: absolute; left: 205px; top: 58px;
    font-family: "Pinyon Script", "Times New Roman", cursive;
    font-size: 44px; color: var(--gold); white-space: nowrap;
  }
  .card-front .contact {
    position: absolute; left: 255px; top: 152px;
    color: var(--text-light); font-size: 16px; line-height: 1.45;
  }
  .card-front .contact .label { color: var(--gold); }
  .card-front .address { margin-top: 14px; text-align: center; margin-left: -8px; }
  .card-front .emblem-art {
    position: absolute; left: 0; bottom: 0; width: 230px; height: 175px;
    background: radial-gradient(ellipse at 40% 65%, var(--gold) 0%, var(--gold-deep) 45%, rgba(201,169,14,0) 78%);
    opacity: .9;
  }

  /* Back */
  .card-back .faint-motif {
    position: absolute; left: 150px; top: 0; width: 260px; height: 300px;
    background: radial-gradient(ellipse at center, rgba(255,255,255,.07) 0%, rgba(255,255,255,0) 70%);
  }
  .card-back .appointment-band {
    position: absolute; left: 0; right: 0; top: 68px; height: 150px;
    background: var(--band-white); color: var(--ink);
    padding: 14px 34px 0;
  }
  .appointment-band .title {
    text-align: center; font-weight: 700; font-size: 19px; margin-bottom: 8px;
  }
  .appointment-band .field-row {
    display: flex; align-items: baseline; font-size: 13px; font-weight: 600; margin-bottom: 8px;
  }
  .appointment-band .field-line {
    flex: 1; border-bottom: 2px dotted var(--dots); margin: 0 4px; height: 1px;
  }
  .appointment-band .field-line.short { flex: 0 0 150px; }
  .appointment-band .notice { font-size: 13px; font-weight: 600; margin-top: 10px; }
</style>
</head>
<body>
<main class="canvas">
  <section class="card card-front">
    <div class="emblem-art" role="img" aria-label="Gold scissors and comb illustration with swirl ornaments"></div>
    <h1 class="salon-name">Marisol Denby</h1>
    <div class="contact">
      <p class="phone"><span class="label">Phone:</span> 717-555-0148</p>
      <p class="address">362 Thistledown lane York,<br>Pa.17488</p>
    </div>
  </section>

  <section class="card card-back">
    <div class="faint-motif" role="img" aria-label="Faint scissors and comb decoration"></div>
    <div class="appointment-band">
      <h2 class="title">Your Next Appointment is</h2>
      <div class="field-row"><span>Name:</span><span class="field-line"></span></div>
      <div class="field-row"><span>Date:</span><span class="field-line short"></span><span>Time:</span><span class="field-line"></span></div>
      <p class="notice">If unable to keep appointment, kindly give 24hrs notice.</p>
    </div>
  </section>
</main>
</body>
</html>
```